I am looking for a Business Card Design for my spirit company titled "Harbor Pour Co" The company specializes in prohibition style/speakeasy mixology drinks and alcohol distribution. I am looking for Retro, Masculine, Sophisticated Card that embodies the look of Prohibition. Black and White colors. Also add Facebook, Instgram logo

Information that should go on the card is my Name, Title, Phone, Email, Website as follows:

Tobias K Verran
Principal
301.555.0187
tobias@harborpourco.example
harborpourco.example
Updates

Hello all I have uploaded a pdf version of the logo. It seems as if some are saying the resolution is too small.

Target Market(s)

Male and Female drinkers of all ages with a sophisticated palate that have an appreciation for fine crafted cocktail

Industry/Entity Type

Business

Requirements
Must have
• Information that should go on the card is my Name, Title, Phone, Email, Website as follows:

Tobias K Verran
Principal
301.555.0187
tobias@harborpourco.example
harborpourco.example

```html
<!DOCTYPE html>
<html lang="en">
<head>
<meta charset="utf-8">
<title>Harbor Pour Co — Business Card</title>
<link rel="stylesheet" href="https://fonts.googleapis.com/css2?family=Roboto:wght@300;400&display=swap">
<style>
  :root {
    --backdrop: #2e2e2e;
    --card-white: #ffffff;
    --panel-dark: #3a3a3a;
    --ink: #2c2c2c;
    --name-text: #d4d4d4;
    --muted-text: #9c9c9c;
    --contact-text: #c9c9c9;
  }
  * { box-sizing: border-box; margin: 0; padding: 0; }
  html, body {
    width: 1200px; height: 900px; overflow: hidden;
    background: var(--backdrop);
    font-family: "Roboto", Arial, sans-serif;
  }
  .canvas { position: relative; width: 1200px; height: 900px; }
  .card {
    position: absolute; left: 285px; width: 630px; height: 360px;
    background: var(--card-white); overflow: hidden;
    box-shadow: 0 10px 24px rgba(0,0,0,0.35);
  }
  .card--front { top: 60px; }
  .card--back { top: 480px; display: flex; }
  .brand {
    position: absolute; display: flex; align-items: center; justify-content: center;
  }
  .brand__name {
    font-weight: 300; color: var(--ink);
    text-transform: uppercase; text-align: center;
    line-height: 1.15;
  }
  .brand__name span { display: block; }
  .card--front .brand { left: 0; top: 0; width: 630px; height: 360px; }
  .card--front .brand__name { font-size: 40px; letter-spacing: 8px; }
  .back__logo-side { position: relative; width: 265px; height: 100%; background: var(--card-white); }
  .back__logo-side .brand { left: 0; top: 0; width: 265px; height: 360px; }
  .back__logo-side .brand__name { font-size: 26px; letter-spacing: 5px; }
  .back__info {
    flex: 1; background: var(--panel-dark);
    padding: 58px 0 0 42px;
  }
  .person__name { font-size: 30px; font-weight: 300; color: var(--name-text); }
  .person__title { font-size: 13px; font-weight: 300; color: var(--muted-text); margin-top: 4px; }
  .contacts { list-style: none; margin-top: 44px; }
  .contacts li {
    display: flex; align-items: center; gap: 12px;
    font-size: 14px; font-weight: 300; color: var(--contact-text);
    margin-bottom: 7px;
  }
  .contacts svg { width: 14px; height: 14px; flex: none; }
</style>
</head>
<body>
<main class="canvas">
  <section class="card card--front" aria-label="Card front">
    <div class="brand">
      <p class="brand__name"><span>Harbor</span><span>Pour Co</span></p>
    </div>
  </section>

  <section class="card card--back" aria-label="Card back">
    <div class="back__logo-side">
      <div class="brand">
        <p class="brand__name"><span>Harbor</span><span>Pour Co</span></p>
      </div>
    </div>
    <div class="back__info">
      <h1 class="person__name">Tobias K Verran</h1>
      <p class="person__title">Principal</p>
      <ul class="contacts">
        <li>
          <svg viewBox="0 0 16 16" aria-hidden="true"><path fill="#fff" d="M3 1h3l1.5 4-2 1.2a9 9 0 0 0 4.3 4.3L11 8.5l4 1.5v3a2 2 0 0 1-2 2A13 13 0 0 1 1 3a2 2 0 0 1 2-2z"/></svg>
          <span>301.555.0187</span>
        </li>
        <li>
          <svg viewBox="0 0 16 16" aria-hidden="true"><rect x="1" y="3" width="14" height="10" fill="#fff"/><path d="M1 3l7 6 7-6" fill="none" stroke="#3a3a3a" stroke-width="1.4"/></svg>
          <span>tobias@harborpourco.example</span>
        </li>
        <li>
          <svg viewBox="0 0 16 16" aria-hidden="true"><circle cx="8" cy="8" r="7" fill="#fff"/><g fill="none" stroke="#3a3a3a" stroke-width="1"><ellipse cx="8" cy="8" rx="3" ry="7"/><path d="M1 8h14M2.5 4.5h11M2.5 11.5h11"/></g></svg>
          <span>harborpourco.example</span>
        </li>
      </ul>
    </div>
  </section>
</main>
</body>
</html>
```